Business card design reauest

2 sided. White on both sides

Martin Oakhurst

Ho Chi Minh, Vietnam

Cell Phone / Whatsapp/ Wechat/Zalo
1-555-382-7194
Moakhurst@kvpartsline.vn
Www.kvpartsline.vn
Www.kvpartsline.com

Industry/Entity Type

Sofa and furniture and kitchen

Contact Information for Business Card

2 sided. White on both sides Martin Oakhurst Ho Chi Minh, Vietnam Cell Phone / Whatsapp/ Wechat/Zalo 1-555-382-7194 Moakhurst@kvpartsline.vn Www.kvpartsline.vn Www.kvpartsline.com

```html
<!DOCTYPE html>
<html lang="en">
<head>
<meta charset="utf-8">
<title>KV Partsline – Business Card</title>
<link rel="stylesheet" href="https://fonts.googleapis.com/css2?family=EB+Garamond:wght@500;600&display=swap">
<style>
  :root {
    --green: #009a3a;
    --ink: #231f20;
    --paper: #ffffff;
    --backdrop: #e8e7e4;
  }
  html, body {
    margin: 0;
    padding: 0;
    width: 1181px;
    height: 1200px;
    overflow: hidden;
    background: var(--backdrop);
  }
  .canvas {
    position: relative;
    width: 1181px;
    height: 1200px;
  }
  .card {
    position: absolute;
    left: 217px;
    width: 747px;
    height: 427px;
    background: var(--paper);
    box-shadow: 0 6px 18px rgba(0,0,0,0.12);
    font-family: "EB Garamond", Georgia, serif;
    color: var(--ink);
    overflow: hidden;
  }
  .card--front { top: 128px; }
  .card--back  { top: 652px; }

  .bar { position: absolute; }
  .bar--top-ink    { left: 0; top: 0; width: 314px; height: 8px; background: var(--ink); }
  .bar--top-green  { left: 0; top: 14px; width: 205px; height: 9px; background: var(--green); }
  .bar--foot-green { right: 0; top: 404px; width: 205px; height: 9px; background: var(--green); }
  .bar--foot-ink   { right: 0; bottom: 0; width: 314px; height: 9px; background: var(--ink); }

  .holder-name {
    position: absolute;
    left: 42px;
    top: 52px;
    margin: 0;
    font-size: 40px;
    font-weight: 600;
    line-height: 1;
    color: var(--green);
    letter-spacing: 0.5px;
  }
  .holder-city {
    position: absolute;
    left: 43px;
    top: 92px;
    margin: 0;
    font-size: 19px;
    font-weight: 600;
    letter-spacing: 0.3px;
    text-transform: uppercase;
  }
  .rule {
    position: absolute;
    left: 46px;
    top: 157px;
    width: 100px;
    height: 3px;
    background: var(--ink);
  }

  .contacts {
    position: absolute;
    left: 41px;
    top: 204px;
    margin: 0;
    padding: 0;
    list-style: none;
  }
  .contacts__item {
    display: flex;
    align-items: center;
    height: 26px;
    margin-bottom: 16px;
    font-size: 24px;
    font-weight: 600;
  }
  .contacts__icon {
    width: 26px;
    height: 26px;
    flex: none;
    margin-right: 20px;
  }

  .brand-name {
    position: absolute;
    margin: 0;
    color: var(--green);
    font-weight: 600;
    text-transform: uppercase;
    white-space: nowrap;
    line-height: 1;
  }
  .card--front .brand-name {
    left: 587px;
    top: 118px;
    transform: translateX(-50%);
    font-size: 26px;
    letter-spacing: 0.5px;
  }
  .card--back .brand-name {
    left: 50%;
    top: 50%;
    transform: translate(-50%, -50%);
    font-size: 54px;
    letter-spacing: 1px;
  }
</style>
</head>
<body>
<div class="canvas">

  <section class="card card--front" aria-label="Business card front">
    <div class="bar bar--top-ink"></div>
    <div class="bar bar--top-green"></div>

    <h1 class="holder-name">Martin Oakhurst</h1>
    <p class="holder-city">Ho Chi Minh, Vietnam</p>
    <div class="rule"></div>

    <ul class="contacts">
      <li class="contacts__item">
        <svg class="contacts__icon" viewBox="0 0 26 26" aria-hidden="true">
          <circle cx="13" cy="13" r="13" fill="var(--green)"/>
          <path d="M8.2 6.5l2.4-.4 1.4 3.2-1.6 1.3c.8 1.8 2.2 3.2 4 4l1.3-1.6 3.2 1.4-.4 2.4c-.2.8-1 1.3-1.8 1.2C11 17.4 7.6 14 7 8.3c-.1-.8.4-1.6 1.2-1.8z" fill="#fff"/>
        </svg>
        <span>(555) 382-7194</span>
      </li>
      <li class="contacts__item">
        <svg class="contacts__icon" viewBox="0 0 26 26" aria-hidden="true">
          <circle cx="13" cy="13" r="13" fill="var(--green)"/>
          <rect x="6.5" y="8.5" width="13" height="9" rx="1" fill="#fff"/>
          <path d="M6.8 9l6.2 4.8L19.2 9" fill="none" stroke="var(--green)" stroke-width="1"/>
        </svg>
        <span>Moakhurst@kvpartsline.vn</span>
      </li>
      <li class="contacts__item">
        <svg class="contacts__icon" viewBox="0 0 26 26" aria-hidden="true">
          <circle cx="13" cy="13" r="13" fill="var(--green)"/>
          <g fill="none" stroke="#fff" stroke-width="1.4">
            <circle cx="13" cy="13" r="8.5"/>
            <ellipse cx="13" cy="13" rx="3.8" ry="8.5"/>
            <path d="M4.5 13h17M6 8.8h14M6 17.2h14"/>
          </g>
        </svg>
        <span>Www.kvpartsline.vn</span>
      </li>
      <li class="contacts__item">
        <svg class="contacts__icon" viewBox="0 0 26 26" aria-hidden="true">
          <circle cx="13" cy="13" r="13" fill="var(--green)"/>
          <g fill="none" stroke="#fff" stroke-width="1.4">
            <circle cx="13" cy="13" r="8.5"/>
            <ellipse cx="13" cy="13" rx="3.8" ry="8.5"/>
            <path d="M4.5 13h17M6 8.8h14M6 17.2h14"/>
          </g>
        </svg>
        <span>Www.kvpartsline.com</span>
      </li>
    </ul>

    <p class="brand-name">KV Partsline</p>

    <div class="bar bar--foot-green"></div>
    <div class="bar bar--foot-ink"></div>
  </section>

  <section class="card card--back" aria-label="Business card back">
    <p class="brand-name">KV Partsline</p>
  </section>

</div>
</body>
</html>
```